Modern & Fresh Halvonix Book Cover

Need a creative e-book cover for my book.

Title: Get Halvonix Clear
Subtitle: Learn How To Easily Choose & Enroll in the Perfect Coverage at the Perfect Time.

Target Market(s)

60-70 year olds in the United States

Font styles to use
Sans Serif

Colors
9bcb3c
33a6d7

Requirements
Must have
• Must look modern and fresh.
• Use our company colors www.TarvoLume.com

```html
<!DOCTYPE html>
<html lang="en">
<head>
<meta charset="utf-8">
<title>Get Halvonix Clear — Book Cover</title>
<link rel="stylesheet" href="https://fonts.googleapis.com/css2?family=Anton&family=Roboto+Condensed:wght@500&display=swap">
<style>
  :root {
    --page: #ffffff;
    --cream: #fdfbe8;
    --green: #97c156;
    --blue: #0096d9;
    --white: #ffffff;
    --brand-green: #6fa832;
  }
  html, body {
    margin: 0;
    padding: 0;
    width: 1175px;
    height: 1200px;
    overflow: hidden;
    background: var(--page);
  }
  .cover {
    position: absolute;
    left: 244px;
    top: 122px;
    width: 678px;
    height: 946px;
    overflow: hidden;
    background: var(--cream);
  }
  .cover__backdrop {
    position: absolute;
    inset: 0;
    width: 678px;
    height: 946px;
  }
  .title {
    position: absolute;
    left: 58px;
    top: 58px;
    margin: 0;
    font-family: "Anton", "Impact", sans-serif;
    font-weight: 400;
    font-size: 104px;
    line-height: 93px;
    letter-spacing: -1px;
  }
  .title span { display: block; }
  .title__blue { color: var(--blue); }
  .title__green { color: var(--green); }
  .subtitle {
    position: absolute;
    right: 56px;
    top: 524px;
    width: 420px;
    margin: 0;
    text-align: right;
    font-family: "Roboto Condensed", "Arial Narrow", sans-serif;
    font-weight: 500;
    font-size: 32px;
    line-height: 42px;
    color: var(--white);
  }
  .brand {
    position: absolute;
    left: 48px;
    top: 862px;
    display: flex;
    align-items: center;
    gap: 8px;
    font-family: "Roboto Condensed", "Arial Narrow", sans-serif;
    font-weight: 500;
    font-size: 40px;
    line-height: 1;
    color: var(--brand-green);
  }
  .brand__dot {
    width: 16px;
    height: 16px;
    border-radius: 50%;
    background: var(--blue);
  }
</style>
</head>
<body>
  <div class="cover">
    <svg class="cover__backdrop" viewBox="0 0 678 946" role="img" aria-label="Cream and green background with a faint pattern of healthcare icons">
      <rect width="678" height="946" fill="var(--cream)"/>
      <path d="M413,0 C480,40 530,110 530,189 C530,300 420,360 330,400 C250,440 194,510 194,590 C194,700 320,820 354,946 L678,946 L678,0 Z" fill="var(--green)"/>
    </svg>

    <h1 class="title">
      <span class="title__blue">Get</span>
      <span class="title__green">Halvonix</span>
      <span class="title__blue">Clear</span>
    </h1>

    <p class="subtitle">Learn How To Easily Choose &amp; Enroll in the Perfect Coverage at the Perfect Time</p>

    <div class="brand">
      <span class="brand__dot"></span>
      <span class="brand__name">TarvoLume</span>
    </div>
  </div>
</body>
</html>
```